Block makes the buck for writing

We need a notepad in DIN A4 format which we can give to our customers at events. We, TAVORIK, are active in the field of safe electrical engineering and offer software, hardware, academia and consulting in this field. With our software can be z. For example, you can quickly and easily inventory and document all equipment and equipment. Every tool must be checked in Germany and the test repeated at regular intervals. The appropriate test specifications are stored in our software. In addition to the software, we also offer measuring and testing equipment. In our academy, we also offer seminars on various areas of safe electrical engineering. Our consulting advises companies on the establishment of a legally compliant company organization. If necessary, our experts also take on the temporary function of external responsible electrician. So we offer an all-round package concerning safe electrical engineering. TAVORIK makes working with electricity safe. Every year we offer an event with different workshops. There the users of our software are invited. You can exchange ideas with our lecturers and experts and exchange experiences and tips with each other. For this event we need a writing pad where participants can take their notes throughout the day. In addition, the block should also be used by customers. But it would be nice if he had a special feature / a special feature by which he is particularly happy to use. As basic the block should be branded with our logo and our URL (tavorik.de).

```html
<!DOCTYPE html>
<html lang="en">
<head>
<meta charset="utf-8">
<title>TAVORIK Notepad</title>
<link href="https://fonts.googleapis.com/css2?family=Roboto:wght@400;700&display=swap" rel="stylesheet">
<style>
  :root {
    --backdrop: #717171;
    --cover-top: #fcb236;
    --cover-bottom: #f7922a;
    --paper: #efefef;
    --brand-orange: #f7992c;
    --ink-dark: #555555;
    --ink-mid: #666666;
    --rule: #8a8a8a;
    --white: #ffffff;
  }
  * { margin: 0; padding: 0; box-sizing: border-box; }
  html, body {
    width: 1200px; height: 837px; overflow: hidden;
    background: var(--backdrop);
    font-family: "Roboto", Arial, sans-serif;
  }
  .canvas { position: relative; width: 1200px; height: 837px; }

  .sheet { position: absolute; top: 78px; width: 489px; height: 692px; }

  .cover {
    left: 76px;
    background: linear-gradient(180deg, var(--cover-top), var(--cover-bottom));
  }
  .cover .brand {
    position: absolute; left: 232px; top: 128px;
    display: flex; align-items: center; gap: 12px;
    transform: translateX(-50%);
    left: 245px;
  }
  .cover .brand-name {
    font-weight: 700; font-size: 36px; letter-spacing: 0.5px;
    color: var(--white);
  }
  .cover .brand-dot {
    width: 46px; height: 54px; border-radius: 50%;
    background: var(--white);
  }
  .cover .cover-url {
    position: absolute; left: 0; right: 0; top: 736px; top: 658px;
    text-align: center; font-size: 8px; letter-spacing: 4px;
    color: var(--white);
  }

  .page { left: 637px; background: var(--paper); }
  .page .brand {
    position: absolute; left: 41px; top: 56px;
    display: flex; align-items: center; gap: 8px;
  }
  .page .brand-name {
    font-weight: 700; font-size: 23px; color: var(--ink-dark);
  }
  .page .brand-dot {
    width: 28px; height: 32px; border-radius: 50%;
    background: var(--brand-orange);
  }
  .contact {
    position: absolute; left: 362px; top: 48px;
    border-left: 1px solid #9a9a9a;
    padding-left: 7px;
    font-size: 7.4px; line-height: 9.2px; color: var(--ink-mid);
  }
  .contact .address { margin-bottom: 5px; }
  .contact .item { display: flex; align-items: center; gap: 4px; }
  .contact svg { width: 7px; height: 7px; flex: none; }

  .rules { position: absolute; left: 41px; top: 132px; width: 412px; }
  .rules span {
    display: block; height: 28px;
    border-top: 1px solid var(--rule);
    opacity: 0.75;
  }
</style>
</head>
<body>
<div class="canvas">

  <section class="sheet cover">
    <div class="brand">
      <span class="brand-name">TAVORIK</span>
      <span class="brand-dot"></span>
    </div>
    <p class="cover-url">www.tavorik.de</p>
  </section>

  <section class="sheet page">
    <div class="brand">
      <span class="brand-name">TAVORIK</span>
      <span class="brand-dot"></span>
    </div>

    <address class="contact">
      <div class="address">2145 Birchwood Lane<br>Fairbanks, Alaska 99701</div>
      <div class="item">
        <svg viewBox="0 0 10 10"><path d="M2 1l2 2-1 1.5c.7 1.3 1.6 2.2 2.9 2.9L7.4 6l2 2-1.4 1.5C4.5 9 1 5.5.5 2z" fill="#f7992c"/></svg>
        <span>555-214-7730</span>
      </div>
      <div class="item">
        <svg viewBox="0 0 10 10"><rect x="0.5" y="2" width="9" height="6" fill="#f7992c"/><path d="M0.5 2l4.5 3.5L9.5 2" fill="none" stroke="#fff" stroke-width="0.8"/></svg>
        <span>name@tavorik.de</span>
      </div>
      <div class="item">
        <svg viewBox="0 0 10 10"><circle cx="5" cy="5" r="4.5" fill="#f7992c"/><path d="M0.5 5h9M5 0.5c-2 2.5-2 6.5 0 9M5 0.5c2 2.5 2 6.5 0 9" fill="none" stroke="#fff" stroke-width="0.6"/></svg>
        <span>www.tavorik.de</span>
      </div>
    </address>

    <div class="rules" aria-hidden="true">
      <span></span><span></span><span></span><span></span><span></span>
      <span></span><span></span><span></span><span></span><span></span>
      <span></span><span></span><span></span><span></span><span></span>
      <span></span><span></span><span></span><span></span>
    </div>
  </section>

</div>
</body>
</html>
```